Ferrowave.com website design

I need a basic website for www.ferrowave.com. Ferro Wave has been hosting websites since 2002 via partnership arrangement with Stackhollow.com and Namequarry.com. We do not do any design, only hosting for small companies and nonprofits. We are referring people to PixelGuild and others to get their websites developed. Our website and pricing does not change often, but I need to be able to easily update the pricing and contact page.

Target Market(s)

Small company and non profit organizations

Industry/Entity Type

Utility

Coding

Coded - Design and coding required

Number of Pages Required

5+ page

Colors

Designer to choose colors to be used in the design.

Requirements
Must have
• Wordsmith format for easy content management. The logo attached. Contact us page with the following: Phone and fax are the same number: 888.514.2973. Email address is myferrowave@mailnest.example. Mailing address is 4819 E. Tolliver Bend #317, Searcy, AR 72143.
Nice to have
• Some kind of badge or tag line on the home page that celebrates our 15th year of hosting without a single hosting without any downtime. We are are 15 year partners with Stackhollow.com and Namequarry.com. Website Design tab needs to reference PixelGuild or others for all their website design needs. We provide no design or updating services. We will provide the developers FTP access to our dedicated Linux server. We do not provide email services other than redirects to their proprietary email or gmail, yahoo, etc. Needs a services and pricing tab. We provide domain registration services via our partnership with Namequarry.com. We will want a way for them to submit a suggested domain name for us to verify if available. I might be able to get a link from Namequarry.com to our account for you to include on that tab REGISTER DOMAIN. The tab buttons can be: WHO WE ARE, WHAT WE DO, WHEN YOU NEED US, WHERE TO REACH US. Maybe consider making the WHO, WHAT, WHEN and WHERE a dark blue color the rest of the text different color just so they stand out
Should not have
• A lot of animation that takes a long time to open. Clean and simple website.

```html
<!DOCTYPE html>
<html lang="en">
<head>
<meta charset="utf-8">
<title>Ferro Wave — Who We Are</title>
<link rel="stylesheet" href="https://fonts.googleapis.com/css2?family=Montserrat:wght@400;500;600;700&display=swap">
<style>
  :root {
    --brand-navy: #0A389A;
    --brand-accent: #1A8BFF;
    --brand-blue: #1254B8;
    --tab-start: #0C48A6;
    --tab-end: #1460C6;
    --page-pale: #EAF1F9;
    --card-white: #FFFFFF;
    --text-dark: #3A3A3A;
    --icon-faint: #DDE3EA;
  }
  * { margin: 0; padding: 0; box-sizing: border-box; }
  html, body { width: 1200px; height: 849px; overflow: hidden; }
  body {
    font-family: "Montserrat", sans-serif;
    background: var(--page-pale);
    position: relative;
  }
  .hero-band {
    position: absolute; left: 0; top: 0;
    width: 1200px; height: 562px;
    background: var(--brand-navy);
  }
  .site-logo {
    position: absolute; left: 108px; top: 44px;
    font-size: 44px; font-weight: 600; color: #fff;
    letter-spacing: -0.5px;
  }
  .main-nav a {
    position: absolute; top: 67px;
    font-size: 13px; font-weight: 600; color: #fff;
    text-decoration: none; letter-spacing: 0.2px;
  }
  .main-nav .nav-key { color: var(--brand-accent); }
  .nav-who { left: 580px; }
  .nav-what { left: 749px; }
  .nav-when { left: 918px; }
  .nav-active-dot {
    position: absolute; left: 619px; top: 94px;
    width: 5px; height: 5px; border-radius: 50%;
    background: var(--brand-accent);
  }
  .hero-headline {
    position: absolute; left: 0; top: 190px; width: 1200px;
    text-align: center; color: #fff;
    font-size: 45px; font-weight: 500; line-height: 53px;
    letter-spacing: 0.2px;
  }
  .hero-headline .highlight { color: var(--brand-accent); }

  .stat-badge {
    position: absolute; top: 476px;
    width: 169px; height: 169px; border-radius: 50%;
    background: #fff;
    box-shadow: 0 6px 18px rgba(10, 40, 90, 0.12);
    overflow: hidden;
  }
  .stat-years { left: 65px; }
  .stat-satisfaction { left: 412px; }
  .stat-icon { position: absolute; }
  .stat-value, .stat-unit, .stat-caption { position: absolute; color: var(--brand-blue); }
  .stat-value { font-weight: 700; }
  .years-value { left: 96px; top: 528px; font-size: 60px; line-height: 60px; letter-spacing: -1px; }
  .years-unit { left: 95px; top: 583px; font-size: 22px; font-weight: 500; }
  .satisfaction-value { left: 452px; top: 571px; font-size: 37px; font-weight: 600; }
  .stat-caption {
    top: 619px; font-size: 14px; font-weight: 500; color: var(--text-dark);
  }
  .years-caption { left: 126px; }
  .satisfaction-caption { left: 474px; }

  .about-card {
    position: absolute; left: 712px; top: 444px;
    width: 411px; height: 366px;
    background: var(--card-white);
    box-shadow: 0 6px 20px rgba(10, 40, 90, 0.10);
  }
  .about-tab {
    position: absolute; left: 712px; top: 429px;
    width: 340px; height: 58px; overflow: hidden;
  }
  .about-tab svg { position: absolute; left: 0; top: 0; }
  .about-title {
    position: absolute; left: 15px; top: 14px;
    font-size: 47px; font-weight: 700; color: #fff;
    line-height: 47px; letter-spacing: 0.5px; white-space: nowrap;
  }
  .about-body {
    position: absolute; left: 735px; width: 366px;
    font-size: 15px; font-weight: 500; line-height: 18.4px;
    color: var(--text-dark);
  }
  .about-lead { top: 518px; }
  .about-second { top: 644px; }
  .about-third { top: 716px; }
</style>
</head>
<body>
  <div class="hero-band"></div>

  <header>
    <div class="site-logo">logo</div>
    <nav class="main-nav">
      <a class="nav-who" href="#who"><span class="nav-key">WHO</span> WE ARE</a>
      <a class="nav-what" href="#what"><span class="nav-key">WHAT</span> WE DO</a>
      <a class="nav-when" href="#when"><span class="nav-key">WHEN</span> YOU NEED US</a>
    </nav>
    <span class="nav-active-dot"></span>
  </header>

  <h1 class="hero-headline">
    Suspendisse <span class="highlight">consequat volutpat</span> egestas.<br>
    Aliquam vulputate in eros at egestas.
  </h1>

  <section class="stats">
    <div class="stat-badge stat-years">
      <svg class="stat-icon" style="left:105px;top:20px" width="64" height="100" viewBox="0 0 64 100" role="img" aria-label="Faint thumbs-up icon">
        <path d="M8 48 h14 v44 h-14 z M22 50 l14 -30 c4 -6 10 -2 9 4 l-3 20 h20 v48 h-40" fill="none" stroke="var(--icon-faint)" stroke-width="4" stroke-linejoin="round"/>
        <path d="M12 12 l10 10 M2 30 h12" stroke="var(--icon-faint)" stroke-width="4" stroke-linecap="round"/>
      </svg>
    </div>
    <div class="stat-badge stat-satisfaction">
      <svg class="stat-icon" style="left:55px;top:25px" width="114" height="100" viewBox="0 0 114 100" role="img" aria-label="Faint customers icon">
        <circle cx="40" cy="30" r="14" fill="none" stroke="var(--icon-faint)" stroke-width="4"/>
        <path d="M6 90 c0 -26 14 -36 34 -36 s34 10 34 36" fill="none" stroke="var(--icon-faint)" stroke-width="4"/>
        <circle cx="80" cy="22" r="18" fill="none" stroke="#E3EEFB" stroke-width="4"/>
        <path d="M40 92 c0 -30 18 -44 40 -44 s40 14 40 44" fill="none" stroke="#E3EEFB" stroke-width="4"/>
      </svg>
    </div>
    <div class="stat-value years-value">15</div>
    <div class="stat-unit years-unit">Years</div>
    <div class="stat-caption years-caption">of experience in web hosting</div>
    <div class="stat-value satisfaction-value">98%</div>
    <div class="stat-caption satisfaction-caption">customer’s satisfaction</div>
  </section>

  <section class="about">
    <div class="about-card"></div>
    <div class="about-tab">
      <svg width="340" height="58" viewBox="0 0 340 58">
        <defs>
          <linearGradient id="tabFill" x1="0" y1="0" x2="1" y2="0">
            <stop offset="0" stop-color="var(--tab-start)"/>
            <stop offset="1" stop-color="var(--tab-end)"/>
          </linearGradient>
        </defs>
        <polygon points="33,0 336,0 321,58 18,58" fill="url(#tabFill)"/>
      </svg>
      <h2 class="about-title">ABOUT US</h2>
    </div>
    <p class="about-body about-lead">Suspendisse consequat volutpat egestas. Ali-quam vulputate in eros at egestas, vitae portti-tor orci pharetra ut. Nunc consectetur vel eros ac vehicula. Phasellus massa nibh, bibendum vitae erat ac, interdum accumsan quam.</p>
    <p class="about-body about-second">Donec in dolor auctor, rhosus nibh arcu, in port-titor ipsum viverra ut. Etiam eu dui nisi. Duis tincidunt efficitur libero at condimentum.</p>
    <p class="about-body about-third">Donec in dolor auctor, rhosus nibh arcu, in port-titor ipsum viverra ut. Etiam eu dui nisi. Duis tincidunt efficitur libero at condimentum.</p>
  </section>
</body>
</html>
```